Holiday Rental Company Flyer Design (DL not A5)

Note from PixelFolk Administration: The category sizing selected is A5, however the project requires DL sized artwork. Please refer to the DL template link below while the 'Special Requirements' are updated accordingly.

Project Brief:
We need a double sided DL flyer designed for an up market Holiday Rental Company that portrays a personalised approach to property management. These are to be used for letter box drops to homes we're specifically targeting so the design should be modern, complimentary colour palette, uncluttered & visually appealing.

Please Download the DL Template from Quillmark here: http://www.quillmark.com.au/qm/ns/propath/UploadResources.aspx?selectedTab=0?pfid=BFB&pf_id=BFB&xnav=easypath-upload-image#Templates

Target Market(s)

Wealthy Home Owners

Industry/Entity Type

It Company

Font styles to use
Other font styles liked:
• Avant Garde Extra Light & Demi

Colors
33b8a4

Requirements
Must have
• DL Flyer sizes (210mm width x 99mm width, plus 3mm bleed)
• Front: Logo, Main Image & Grab
• Back: Contact Details & Brief Description of our business
• Images: Ideally the main image should be the house with the pool but alternatively a lifestyle images could also be used.
Nice to have
• A creative designer!
Should not have
• Clutter & busy designs

```html
<!DOCTYPE html>
<html lang="en">
<head>
<meta charset="utf-8">
<title>Harbourline Stays – DL Flyer</title>
<link rel="stylesheet" href="https://fonts.googleapis.com/css2?family=Poppins:wght@200;300;400;600&display=swap">
<style>
  :root {
    --teal: #1fb59c;
    --teal-soft: #9fd6c9;
    --teal-text: #2aa58f;
    --paper: #ffffff;
    --stage: #e9ecec;
    --night: #2d2a7a;
    --white: #ffffff;
  }
  * { box-sizing: border-box; margin: 0; padding: 0; }
  html, body { width: 1200px; height: 900px; overflow: hidden; }
  body {
    background: var(--stage);
    font-family: "Poppins", sans-serif;
    position: relative;
  }
  .flyer {
    position: absolute;
    left: 195px;
    width: 810px;
    height: 405px;
    background: var(--paper);
    box-shadow: 0 2px 10px rgba(0,0,0,.12);
    overflow: hidden;
  }
  /* Front */
  .flyer--front { top: 40px; padding: 17px 18px; }
  .hero {
    position: relative;
    width: 100%;
    height: 100%;
    background:
      linear-gradient(90deg, rgba(70,55,30,.95) 0%, rgba(150,120,70,.85) 22%, rgba(60,50,120,.4) 40%, transparent 55%),
      linear-gradient(160deg, #2a2676 0%, #3b37a0 45%, #5e5cc4 70%, #2f7fd6 100%);
  }
  .hero__pool {
    position: absolute;
    left: 0; right: 0; bottom: 0;
    height: 42px;
    background: linear-gradient(90deg, #1d4fb8, #3b8ef0 50%, #2f63d0);
  }
  .hero__brand {
    position: absolute;
    left: 360px;
    top: 28px;
    width: 290px;
    text-align: center;
    color: var(--teal);
    font-weight: 200;
    font-size: 40px;
    line-height: 44px;
    letter-spacing: 5px;
  }
  .hero__mark {
    display: block;
    width: 38px; height: 38px;
    margin: 14px auto 0;
    border: 1.5px solid var(--white);
    border-radius: 50%;
    opacity: .85;
  }
  .hero__grab {
    margin-top: 30px;
    color: var(--white);
    font-weight: 300;
    font-size: 15px;
    line-height: 19px;
    letter-spacing: 0;
  }
  /* Back */
  .flyer--back { top: 465px; }
  .headline {
    position: absolute;
    left: 33px; top: 28px;
    color: var(--teal);
    line-height: 1;
  }
  .headline__light { display: block; font-weight: 200; font-size: 60px; letter-spacing: -1px; }
  .headline__bold { display: block; font-weight: 600; font-size: 60px; letter-spacing: -2px; margin-top: 6px; }
  .photo {
    position: absolute;
    width: 74px; height: 74px;
    border-radius: 50%;
  }
  .photo--flowers { left: 32px; top: 178px; width: 96px; height: 96px; background: radial-gradient(circle at 40% 40%, #d9893a, #7a6a55 60%, #4a4a48); }
  .photo--boat { left: 490px; top: 30px; background: linear-gradient(180deg, #b7cfe0, #7ba3c4 60%, #5c86a9); }
  .photo--swim { left: 490px; top: 114px; background: radial-gradient(circle, #5fc6d6, #2c9bb4); }
  .photo--basin { left: 490px; top: 200px; background: radial-gradient(circle at 50% 60%, #e6e2dc, #a8a49f); }
  .greet {
    position: absolute;
    left: 146px; top: 192px;
    width: 320px;
    color: var(--teal-text);
    font-weight: 300;
    font-size: 13.5px;
    line-height: 17px;
  }
  .greet__lead { display: block; font-size: 20px; line-height: 24px; margin-top: 4px; font-weight: 400; }
  .service {
    position: absolute;
    left: 580px; top: 30px;
    width: 210px;
    color: var(--teal-text);
    font-weight: 300;
    font-size: 13.5px;
    line-height: 17px;
  }
  .service strong { font-weight: 600; }
  .service ul { list-style: none; margin-top: 8px; }
  .service li { position: relative; padding-left: 12px; margin-bottom: 6px; }
  .service li::before { content: "•"; position: absolute; left: 0; }
  .footer {
    position: absolute;
    left: 0; right: 0; bottom: 0;
    height: 105px;
    background: var(--teal-soft);
  }
  .footer__brand {
    position: absolute;
    left: 40px; top: 24px;
    display: flex; align-items: center; gap: 18px;
    color: var(--teal);
    font-weight: 300;
    font-size: 28px;
    line-height: 30px;
    letter-spacing: 1px;
  }
  .footer__mark { width: 46px; height: 46px; border: 2px solid var(--teal); border-radius: 50%; }
  .footer__invite {
    position: absolute;
    left: 352px; top: 20px;
    width: 190px;
    color: var(--white);
    font-size: 11.5px;
    line-height: 17px;
  }
  .contact {
    position: absolute;
    left: 570px; top: 18px;
    list-style: none;
    color: var(--white);
    font-size: 11.5px;
    line-height: 17px;
  }
  .contact li { display: flex; align-items: center; gap: 6px; }
  .contact svg { width: 11px; height: 11px; fill: var(--teal); flex: none; }
</style>
</head>
<body>
  <section class="flyer flyer--front">
    <div class="hero" role="img" aria-label="Photograph of a modern holiday home at dusk with a lit courtyard and swimming pool">
      <div class="hero__pool"></div>
      <div class="hero__brand">
        HARBOURLINE<br>STAYS
        <span class="hero__mark"></span>
        <p class="hero__grab">Holiday Rental Management<br>with a difference</p>
      </div>
    </div>
  </section>

  <section class="flyer flyer--back">
    <h1 class="headline">
      <span class="headline__light">WHAT WE DO</span>
      <span class="headline__bold">DIFFERENTLY!</span>
    </h1>

    <div class="photo photo--flowers" role="img" aria-label="Photograph of a flower arrangement on a table"></div>
    <p class="greet">Rather than relying upon a key safe or a central pick-up destination, a 'Harbourline Stays' staff member
      <span class="greet__lead">will greet guests upon arrival</span></p>

    <div class="photo photo--boat" role="img" aria-label="Photograph of a sailboat on calm water"></div>
    <div class="photo photo--swim" role="img" aria-label="Photograph of swimmers in clear blue water"></div>
    <div class="photo photo--basin" role="img" aria-label="Photograph of a bathroom basin with flowers"></div>

    <div class="service">
      <p>Our <strong>'Meet &amp; Greet'</strong> service provides home owners with an increased level of Security and also allows us to:</p>
      <ul>
        <li>Prepare the home for their arrival (lights, heaters, music etc.)</li>
        <li>Establish a rapport &amp; help facilitate future bookings</li>
        <li>Reiterate their responsibilities to ensure the return of their bond</li>
      </ul>
    </div>

    <footer class="footer">
      <div class="footer__brand"><span class="footer__mark"></span><span>HARBOURLINE<br>STAYS</span></div>
      <p class="footer__invite">If you'd like to know what your property could achieve or require additional information, please contact us on:</p>
      <ul class="contact">
        <li><svg viewBox="0 0 10 10"><path d="M5 0a3.5 3.5 0 0 0-3.5 3.5C1.5 6 5 10 5 10s3.5-4 3.5-6.5A3.5 3.5 0 0 0 5 0zm0 5a1.4 1.4 0 1 1 0-2.8A1.4 1.4 0 0 1 5 5z"/></svg>PO Box 18, Kelso Bay Victoria 3990</li>
        <li><svg viewBox="0 0 10 10"><circle cx="5" cy="5" r="5"/><path d="M3 3.2c.3 1.6 1.5 2.9 3.3 3.6l.7-.8-1-.6-.5.4c-.7-.4-1.2-.9-1.5-1.6l.4-.5-.6-1z" fill="#fff"/></svg>(03)5900 1427</li>
        <li><svg viewBox="0 0 10 10"><circle cx="5" cy="5" r="5"/><path d="M2.5 3.3h5v3.4h-5zM2.5 3.3L5 5.3l2.5-2" fill="none" stroke="#fff" stroke-width=".7"/></svg>stay@harbourlinestays.com.au</li>
        <li><svg viewBox="0 0 10 10"><circle cx="5" cy="5" r="5"/><path d="M5 1.5v7M1.5 5h7M5 1.5c-2 2-2 5 0 7M5 1.5c2 2 2 5 0 7" fill="none" stroke="#fff" stroke-width=".6"/></svg>www.harbourlinestays.com.au</li>
      </ul>
    </footer>
  </section>
</body>
</html>
```